Business Card Design for Bright Canvas Hue Designs

I need a business card design for Artist Marlon Ketch who specializes in Digital Fine Art, Digital Illustration, Murals and Mixed Media. Digital art techniques combine the use of a computer and specialized programs coupled with the same methods and theories used to produce traditional art. The final design should use the new logo that was just deigned and reflect an artist who has embraced the evolution of art by using modern technology to paint vibrant, stunning and high quality art. Please make this a double sided card and use the attached photo on the back of the card. Please include the name of the business: Bright Canvas Hue Designs, Artist: Marlon Ketch, Phone: 555-283-7190 Website: brightcanvashuedesigns.example

Target Market(s)

Anyone looking for fine art for there home or business.

Industry/Entity Type

Computer

Contact Information for Business Card

This should be a double sided business card with a modern feel to it.

Font styles to use
Sans Serif

Requirements
Must have
• Artist Name: Marlon Ketch
• Business Name and Logo: Bright Canvas Hue Designs
• Phone: 555-283-7190
• Website: brightcanvashuedesigns.example
• specializes in Digital Fine Art, Digital Illustration, Murals and Mixed Media
Nice to have
• Black background with new logo that is attached to file

```html
<!DOCTYPE html>
<html lang="en">
<head>
<meta charset="utf-8">
<title>Bright Canvas Hue Designs – Business Card</title>
<link rel="stylesheet" href="https://fonts.googleapis.com/css2?family=Open+Sans:wght@400;600&display=swap">
<style>
  :root {
    --page-bg: #e9e6e1;
    --card-black: #0d0d0f;
    --card-charcoal: #1c1c20;
    --brand-blue: #5b63d8;
    --name-blue: #6a74e6;
    --text-light: #f2f2f4;
    --accent-purple: #a73bd0;
    --accent-red: #e0404a;
    --koi-yellow: #d9e05a;
    --koi-pink: #d64fa8;
    --koi-blue: #4aa8e0;
    --wave-blue: #9ccbe0;
  }
  * { box-sizing: border-box; margin: 0; padding: 0; }
  html, body { width: 1200px; height: 1023px; overflow: hidden; }
  body {
    background: var(--page-bg);
    font-family: "Open Sans", Arial, sans-serif;
    display: flex;
    flex-direction: column;
    align-items: center;
    justify-content: center;
    gap: 60px;
  }
  .card {
    position: relative;
    width: 700px;
    height: 400px;
    border-radius: 6px;
    overflow: hidden;
    background: linear-gradient(135deg, var(--card-charcoal), var(--card-black) 60%);
    box-shadow: 0 10px 30px rgba(0,0,0,0.25);
  }
  .brand {
    display: flex;
    align-items: center;
    gap: 12px;
    color: var(--brand-blue);
    font-weight: 600;
    font-size: 26px;
  }
  .brand-mark { width: 16px; height: 16px; background: var(--brand-blue); }

  /* Front */
  .front .brand { position: absolute; left: 48px; top: 52px; }
  .front .artist-name {
    position: absolute; left: 48px; top: 118px;
    color: var(--name-blue); font-weight: 600; font-size: 30px;
    letter-spacing: 1px; text-transform: uppercase;
  }
  .contact-list {
    position: absolute; left: 48px; top: 178px;
    list-style: none; display: flex; flex-direction: column; gap: 14px;
    color: var(--text-light); font-size: 22px;
  }
  .contact-list li { display: flex; align-items: center; gap: 12px; }
  .contact-icon {
    width: 20px; height: 20px; border-radius: 3px; background: var(--accent-red);
    display: flex; align-items: center; justify-content: center;
  }
  .specialty-band {
    position: absolute; left: 0; right: 0; bottom: 36px; height: 48px;
    background: var(--accent-purple);
    border-radius: 0 24px 24px 0 / 0 20px 20px 0;
    display: flex; align-items: center; padding-left: 48px;
    color: var(--text-light); font-size: 19px;
  }

  /* Back */
  .koi-artwork {
    position: absolute; left: 120px; top: 0; width: 580px; height: 400px;
    background:
      radial-gradient(ellipse 45% 55% at 42% 52%, var(--koi-yellow), var(--koi-pink) 45%, rgba(74,168,224,0) 75%),
      linear-gradient(120deg, var(--wave-blue), var(--koi-blue) 55%, var(--card-black) 100%);
    clip-path: polygon(18% 0, 100% 0, 100% 78%, 55% 100%, 0 72%);
    opacity: 0.9;
  }
  .back .brand { position: absolute; left: 40px; bottom: 40px; font-size: 22px; }
</style>
</head>
<body>
  <section class="card front" aria-label="Business card front">
    <div class="brand"><span class="brand-mark"></span>Bright Canvas Hue Designs</div>
    <p class="artist-name">Marlon Ketch</p>
    <ul class="contact-list">
      <li>
        <span class="contact-icon">
          <svg width="12" height="12" viewBox="0 0 24 24" aria-hidden="true"><path fill="#fff" d="M6.6 10.8a15 15 0 0 0 6.6 6.6l2.2-2.2a1 1 0 0 1 1-.25 11.4 11.4 0 0 0 3.6.6 1 1 0 0 1 1 1V20a1 1 0 0 1-1 1A17 17 0 0 1 3 4a1 1 0 0 1 1-1h3.5a1 1 0 0 1 1 1c0 1.25.2 2.45.6 3.6a1 1 0 0 1-.25 1z"/></svg>
        </span>555-283-7190
      </li>
      <li>
        <span class="contact-icon">
          <svg width="12" height="12" viewBox="0 0 24 24" aria-hidden="true"><circle cx="12" cy="12" r="9" fill="none" stroke="#fff" stroke-width="2.4"/><path d="M3 12h18M12 3c3 3 3 15 0 18M12 3c-3 3-3 15 0 18" fill="none" stroke="#fff" stroke-width="2"/></svg>
        </span>brightcanvashuedesigns.example
      </li>
    </ul>
    <p class="specialty-band">Specializes in Digital Fine Art, Digital Illustration, Murals and Mixed Media</p>
  </section>

  <section class="card back" aria-label="Business card back">
    <div class="koi-artwork" role="img" aria-label="Colourful koi fish illustration swimming among stylised blue waves"></div>
    <div class="brand"><span class="brand-mark"></span>Bright Canvas Hue Designs</div>
  </section>
</body>
</html>
```